Business Card Design

We need a business card design for a Executive search firm based in London & the North East called Kelmscott. We specialise in mid - snr level (£50k - £200k) IT placements. Our company colour is navy blue.

Target Market(s)

CEO, HR Director, Sales Director/VP - (35 - 50), well educated, British, European & American

Industry/Entity Type

Business

Contact Information for Business Card

Kelmscott Talent Limited, Simon Trewella
Mobile - 0044 7700 318 642
London Office - Kelmscott House, 17 Birchcombe, Pinner. HA5 3QX
Tel: 00 44 20 718 46203
North East Office – Veltris Centre, Marlowe Lane, Hebburn, NE31 4GT
Tel: 00 44 191 4826053
www.kelmscotttalent-example.com

Also the same details for my Business Partner Ravi Sotkar
with his mobile number as 0044 7700 582731

Requirements
Must have
• must have the same logo

the logo needs to be the same but made sharper

```html
<!DOCTYPE html>
<html lang="en">
<head>
<meta charset="utf-8">
<title>Kelmscott Talent Limited – Business Card</title>
<link rel="stylesheet" href="https://fonts.googleapis.com/css2?family=Lato:wght@400;700&display=swap">
<style>
  :root {
    --navy: #1d3a66;
    --navy-soft: #4a6590;
    --taupe: #9b8e89;
    --band-grey: #ebe8e7;
    --text-grey: #8a7f7a;
    --paper: #ffffff;
    --backdrop: #d9dadc;
  }
  * { box-sizing: border-box; margin: 0; padding: 0; }
  html, body { width: 1200px; height: 926px; overflow: hidden; }
  body {
    background: var(--backdrop);
    font-family: "Lato", sans-serif;
    position: relative;
  }
  .card {
    position: absolute;
    left: 280px;
    width: 640px;
    height: 376px;
    background: var(--paper);
    overflow: hidden;
    box-shadow: 0 6px 18px rgba(0,0,0,0.18);
  }
  .card--front { top: 48px; }
  .card--back { top: 486px; }

  .wordmark {
    display: flex;
    align-items: center;
    gap: 8px;
    color: var(--navy);
    font-weight: 400;
    font-size: 20px;
    letter-spacing: 0.5px;
  }
  .wordmark__dot {
    width: 14px; height: 14px; border-radius: 50%;
    background: var(--navy-soft);
  }

  /* Front */
  .card--front .wordmark { position: absolute; left: 34px; top: 36px; }
  .person {
    position: absolute; right: 34px; top: 58px; text-align: right;
  }
  .person__name {
    color: var(--navy); font-size: 26px; letter-spacing: 1.5px;
    font-weight: 400; text-transform: uppercase;
  }
  .person__name strong { font-weight: 700; }
  .contact-line {
    display: flex; justify-content: flex-end; align-items: center; gap: 8px;
    color: var(--text-grey); font-size: 15px; letter-spacing: 0.6px;
    margin-top: 4px;
  }
  .contact-line svg { width: 16px; height: 16px; flex: none; }
  .company-band {
    position: absolute; left: 0; right: 0; top: 160px; height: 48px;
    background: var(--band-grey);
    display: flex; align-items: center; justify-content: center;
  }
  .company-band__name { color: var(--navy); font-size: 30px; letter-spacing: 0.5px; }
  .office { position: absolute; font-size: 13px; color: var(--text-grey); line-height: 1.3; }
  .office__title { color: var(--navy); font-size: 17px; margin-bottom: 2px; }
  .office--london { left: 34px; top: 220px; }
  .office--north-east { right: 34px; top: 250px; text-align: right; }
  .base-stripes { position: absolute; left: 0; bottom: 0; width: 640px; height: 376px; }

  /* Back */
  .card--back .wordmark { position: absolute; left: 50%; top: 52px; transform: translateX(-20%); font-size: 24px; }
  .back-band {
    position: absolute; left: 0; right: 0; top: 138px; height: 182px;
    background: var(--navy); color: var(--paper);
    display: flex; flex-direction: column; align-items: center; justify-content: center; gap: 14px;
  }
  .back-band__name { font-size: 34px; letter-spacing: 0.5px; }
  .back-band__web { font-size: 15px; letter-spacing: 1.5px; }
</style>
</head>
<body>

<section class="card card--front" aria-label="Business card front">
  <svg class="base-stripes" viewBox="0 0 640 376" aria-hidden="true">
    <polygon points="0,300 640,338 640,376 0,376" fill="var(--navy)"/>
    <polygon points="310,334 640,334 640,376 270,376" fill="var(--paper)"/>
    <polygon points="322,340 640,340 640,376 290,376" fill="var(--taupe)"/>
  </svg>

  <div class="wordmark"><span>Kelmscott</span><span class="wordmark__dot"></span></div>

  <div class="person">
    <h1 class="person__name">Simon <strong>Trewella</strong></h1>
    <p class="contact-line">0044 7700 318 642
      <svg viewBox="0 0 16 16"><circle cx="8" cy="8" r="8" fill="var(--navy)"/><rect x="5.5" y="3.5" width="5" height="9" rx="1" fill="none" stroke="#fff" stroke-width="1.2"/></svg>
    </p>
    <p class="contact-line">www.kelmscotttalent-example.com
      <svg viewBox="0 0 16 16"><circle cx="8" cy="8" r="8" fill="var(--navy)"/><path d="M6 10 L10 6 M7 5 h3 a1 1 0 0 1 1 1 v3 M9 11 h-3 a1 1 0 0 1 -1 -1 v-3" fill="none" stroke="#fff" stroke-width="1.2" stroke-linecap="round"/></svg>
    </p>
  </div>

  <div class="company-band"><p class="company-band__name">Kelmscott Talent Limited</p></div>

  <address class="office office--london">
    <p class="office__title">London Office</p>
    <p>Tel: 00 44 20 718 46203</p>
    <p>Kelmscott House, 17 Birchcombe,</p>
    <p>Pinner. HA5 3QX</p>
  </address>

  <address class="office office--north-east">
    <p class="office__title">North East Office</p>
    <p>Tel: 00 44 191 4826053</p>
    <p>Veltris Centre, Marlowe Lane,</p>
    <p>Hebburn, NE31 4GT</p>
  </address>
</section>

<section class="card card--back" aria-label="Business card back">
  <div class="wordmark"><span>Kelmscott</span><span class="wordmark__dot"></span></div>
  <div class="back-band">
    <p class="back-band__name">Kelmscott Talent Limited</p>
    <p class="back-band__web">www.kelmscotttalent-example.com</p>
  </div>
</section>

</body>
</html>
```